PowerPoint Presentation

We are looking for a new PPT layout template existing of a cover page, three internal pages - one with text bullets, one with a picture/information and one with more of a table for pricing information and the last a last "thank you - contact info" page. Feel free to grab any graphics from our website at www.brightharbor.com

Any product can be chosen from our products page. Colors are cyan and orange and feel free to choose darker backgrounds for the front and end page. Also included in the graphics is our new business card design.

Also note we are updating our website, and have attached a sample of how it looks for reference.

Reason: We are still looking for submissions for our PowerPoint presentation. We have increased the award amount as well.

Target Market(s)

Target market is private industry professionals, public safety organizations, and state and local government agencies.

Industry/Entity Type

Business

Colors
33a6d7
86cae6
cee9f5
f68d4d
f8ba93
fce2d4

```html
<!DOCTYPE html>
<html lang="en">
<head>
<meta charset="utf-8">
<title>Bright Harbor — Presentation Template</title>
<link rel="stylesheet" href="https://fonts.googleapis.com/css2?family=Open+Sans:wght@400;600;700&display=swap">
<style>
  :root {
    --cyan: #05a8ec;
    --cyan-mid: #86cae6;
    --cyan-deep: #33a6d7;
    --orange: #f68d4d;
    --orange-soft: #f8ba93;
    --ink: #333333;
    --grey: #6f6f6f;
    --stage: #ececec;
    --white: #ffffff;
  }
  * { box-sizing: border-box; margin: 0; padding: 0; }
  html, body { width: 1200px; height: 1051px; overflow: hidden; }
  body { background: var(--stage); font-family: "Open Sans", Arial, sans-serif; color: var(--ink); position: relative; }

  .slide { position: absolute; width: 487px; height: 273px; background: var(--white); overflow: hidden; }
  .slide--cover { left: 89px; top: 87px; }
  .slide--bullets { left: 618px; top: 87px; }
  .slide--product { left: 89px; top: 393px; }
  .slide--pricing { left: 618px; top: 393px; }
  .slide--thanks { left: 88px; top: 701px; background: var(--cyan); color: var(--white); text-align: center; }

  .abs { position: absolute; }

  /* cover */
  .cover__brand { left: 0; width: 242px; top: 123px; text-align: center; font-size: 23px; font-weight: 600; color: #6b6b6b; letter-spacing: -0.3px; }
  .cover__panel { left: 242px; top: 0; width: 245px; height: 273px; background: var(--cyan); color: var(--white); }
  .cover__title { left: 62px; top: 121px; font-size: 16px; font-weight: 400; }
  .cover__intro { left: 62px; top: 151px; width: 140px; font-size: 6.3px; line-height: 1.5; }

  /* internal page chrome */
  .page__brand { left: 26px; top: 21px; font-size: 10px; font-weight: 600; color: #666; }
  .page__rule { left: 0; top: 38px; width: 487px; height: 1px; background: var(--orange-soft); }
  .page__number { right: 20px; top: 0; width: 28px; height: 25px; }
  .page__footer { left: 0; bottom: 0; width: 487px; height: 23px; background: var(--orange); }
  .page__tab { left: 24px; bottom: 0; width: 48px; height: 27px; background: var(--white); display: flex; align-items: center; justify-content: center; }
  .page__tab span { width: 12px; height: 12px; border-radius: 50%; background: var(--cyan); }
  .page__url { right: 34px; bottom: 6px; font-size: 7.5px; color: var(--white); }

  /* bullets page */
  .bullets__title { left: 0; width: 487px; top: 52px; text-align: center; font-size: 16px; font-weight: 400; }
  .bullets__lead { left: 100px; width: 287px; top: 76px; text-align: center; font-size: 5.6px; line-height: 1.5; color: var(--grey); }
  .bullets__divider { left: 85px; top: 110px; width: 316px; height: 6px; }
  .bullets__accent { left: 90px; top: 133px; width: 140px; font-size: 5.4px; line-height: 1.55; color: var(--cyan-deep); }
  .bullets__body { left: 90px; top: 194px; width: 140px; font-size: 5.4px; line-height: 1.55; color: var(--grey); }
  .bullets__list { left: 248px; top: 133px; width: 160px; list-style: none; font-size: 5.4px; line-height: 1.5; color: var(--grey); }
  .bullets__list li { position: relative; padding-left: 7px; margin-bottom: 2.5px; }
  .bullets__list li::before { content: ""; position: absolute; left: 0; top: 2.5px; width: 3px; height: 3px; border-radius: 50%; background: var(--ink); }

  /* product page */
  .product__hero { left: 24px; top: 58px; width: 175px; height: 111px; border: 2px solid var(--cyan-mid); padding: 3px; }
  .product__thumb { top: 176px; width: 86px; height: 50px; border: 2px solid var(--cyan-mid); padding: 3px; }
  .product__thumb--a { left: 24px; }
  .product__thumb--b { left: 113px; }
  .product__photo { width: 100%; height: 100%; background: linear-gradient(180deg, #f4f5f6 0%, #d9dcdf 70%, #b9bdc1 100%); position: relative; }
  .product__label { position: absolute; left: 8px; top: 5px; font-size: 5.5px; font-weight: 700; color: #222; }
  .product__label--small { left: 28px; top: 3px; font-size: 3.6px; }
  .product__title { left: 238px; top: 58px; font-size: 16px; font-weight: 400; }
  .product__text { left: 238px; top: 88px; width: 226px; font-size: 5.5px; line-height: 1.6; color: var(--grey); }
  .product__text p { margin-bottom: 6px; }

  /* pricing page */
  .pricing__title { left: 24px; top: 57px; font-size: 14px; font-weight: 400; }
  .price-table { left: 24px; top: 87px; width: 267px; border-collapse: collapse; font-size: 5.4px; text-align: center; }
  .price-table th { background: var(--orange); color: var(--white); font-weight: 600; height: 15px; border-right: 1px solid var(--white); }
  .price-table td { height: 15.2px; border-bottom: 1px solid #555; }
  .price-table tr.is-highlight td { background: var(--cyan-mid); color: var(--white); border-bottom: 1px solid var(--white); }
  .price-table tr.is-total td { background: var(--cyan-deep); color: var(--white); border-bottom: none; }
  .pricing__chart { top: 78px; width: 62px; height: 78px; }
  .pricing__chart--a { left: 312px; }
  .pricing__chart--b { left: 389px; }
  .pricing__note { top: 171px; width: 66px; font-size: 5.4px; line-height: 1.45; color: var(--grey); }
  .pricing__note--a { left: 312px; }
  .pricing__note--b { left: 389px; }

  /* thank you */
  .thanks__title { left: 0; width: 487px; top: 58px; font-size: 17px; font-weight: 400; }
  .thanks__sub { left: 0; width: 487px; top: 84px; font-size: 12px; line-height: 1.3; }
  .thanks__divider { left: 112px; top: 124px; width: 262px; height: 10px; }
  .thanks__text { left: 0; width: 487px; top: 143px; font-size: 10.5px; line-height: 15px; }
  .thanks__mark { left: 235px; top: 220px; width: 16px; height: 16px; border-radius: 50%; border: 1.5px solid var(--white); }

  /* standalone brand */
  .brand-display { left: 650px; top: 846px; width: 440px; text-align: center; font-size: 52px; font-weight: 600; color: #111; letter-spacing: -1px; }
</style>
</head>
<body>

<section class="slide slide--cover">
  <div class="abs cover__brand">BRIGHTHARBOR</div>
  <div class="abs cover__panel">
    <h1 class="abs cover__title">Presentation Title</h1>
    <p class="abs cover__intro">Lorem ipsum dolor sit amet, consectetur adipiscing elit. Duis at posuere augue, vel iaculis nulla. Quisque hendrerit nisi non varius venenatis. Nam tincidunt commodo erat, non facilisis nisi tincidunt quis. Maecenas sollicitudin tristique tellus, eu tristique nibh fringilla vitae.</p>
  </div>
</section>

<section class="slide slide--bullets">
  <div class="abs page__brand">BRIGHTHARBOR</div>
  <div class="abs page__rule"></div>
  <svg class="abs page__number" viewBox="0 0 28 25"><path d="M0 0H28V17L14 25L0 17Z" fill="#f68d4d"/><text x="14" y="13" font-size="8" fill="#fff" text-anchor="middle" font-family="Open Sans, sans-serif">2</text></svg>
  <h2 class="abs bullets__title">Attention Facts</h2>
  <p class="abs bullets__lead">Lorem ipsum dolor sit amet, consectetur adipiscing elit. Curabitur ultricies sagittis lorem, accumsan dignissim mauris condimentum ut. Etiam eleifend in nisi in eleifend.</p>
  <svg class="abs bullets__divider" viewBox="0 0 316 6"><line x1="0" y1="3" x2="150" y2="3" stroke="#bbb"/><circle cx="158" cy="3" r="2" fill="none" stroke="#999"/><line x1="166" y1="3" x2="316" y2="3" stroke="#bbb"/></svg>
  <p class="abs bullets__accent">Nam tempus, libero et consectetur imperdiet, libero justo consectetur neque, et dapibus nunc mi ut urna. Phasellus posuere dui in magna sagittis tincidunt. Phasellus nec eros vel eros blandit interdum vel a purus. Fusce venenatis luctus nisl, eu convallis tortor consectetur non. In lacinia non urna ut eleifend. Nam sodales mi eget facilisis vehicula.</p>
  <p class="abs bullets__body">Consectetur imperdiet, libero justo consectetur neque, et dapibus nunc mi ut urna. Phasellus posuere dui in magna sagittis tincidunt. Phasellus nec eros vel eros blandit interdum vel a purus.</p>
  <ul class="abs bullets__list">
    <li>Lorem ipsum dolor sit amet, consectetur adipiscing elit gravida accumsan.</li>
    <li>Nunc at purus vel erat rhoncus euismod vel ac nulla metus laoreet.</li>
    <li>Cras eget libero eget libero gravida accumsan at venenatis leo.</li>
    <li>Quisque sagittis arcu eu ullamcorper condimentum.</li>
    <li>Donec vehicula magna semper enim porta, vel elementum turpis dignissim.</li>
    <li>Praesent in metus laoreet, suscipit purus vitae, fringilla nisl.</li>
  </ul>
  <div class="abs page__footer"></div>
  <div class="abs page__tab"><span></span></div>
  <div class="abs page__url">www.brightharbor.com</div>
</section>

<section class="slide slide--product">
  <div class="abs page__brand">BRIGHTHARBOR</div>
  <div class="abs page__rule"></div>
  <svg class="abs page__number" viewBox="0 0 28 25"><path d="M0 0H28V17L14 25L0 17Z" fill="#f68d4d"/><text x="14" y="13" font-size="8" fill="#fff" text-anchor="middle" font-family="Open Sans, sans-serif">3</text></svg>
  <div class="abs product__hero">
    <div class="product__photo" role="img" aria-label="Photo of the FIELDLINK R-40 trailer-mounted field communications unit">
      <span class="product__label">FIELDLINK R-40</span>
    </div>
  </div>
  <div class="abs product__thumb product__thumb--a">
    <div class="product__photo" role="img" aria-label="Photo of the FIELDLINK AX Series dish unit">
      <span class="product__label product__label--small">FIELDLINK AX SERIES</span>
    </div>
  </div>
  <div class="abs product__thumb product__thumb--b">
    <div class="product__photo" role="img" aria-label="Photo of a portable FIELDLINK terminal kit">
      <span class="product__label product__label--small">FIELDLINK</span>
    </div>
  </div>
  <h2 class="abs product__title">Attention Facts</h2>
  <div class="abs product__text">
    <p>Sed gravida imperdiet lectus, vel pharetra metus varius at. Vivamus a quam vel quam tristique sagittis. Sed pellentesque elit sit amet purus lobortis fringilla. Aliquam imperdiet ut dui ac dignissim.</p>
    <p>Pellentesque habitant morbi tristique senectus et netus et malesuada fames ac turpis egestas. Curabitur a placerat lorem. Phasellus tempor, mauris eget molestie rutrum, orci lorem sollicitudin urna, vulputate pretium mi magna sit amet mauris.</p>
    <p>Integer fermentum, massa vel dictum laoreet, eros dolor fringilla odio, ac cursus velit quam ut libero. Cras et diam nec tellus ultricies rhoncus imperdiet ut lectus. Maecenas urna mi, hendrerit eu ultricies id, interdum et felis. Fusce porttitor euismod faucibus. Fusce at tincidunt sapien. Duis magna sem, ultrices nec enim quis, sagittis elementum felis. Morbi non convallis diam. Proin nibh odio malesuada.</p>
  </div>
  <div class="abs page__footer"></div>
  <div class="abs page__tab"><span></span></div>
  <div class="abs page__url">www.brightharbor.com</div>
</section>

<section class="slide slide--pricing">
  <div class="abs page__brand">BRIGHTHARBOR</div>
  <div class="abs page__rule"></div>
  <svg class="abs page__number" viewBox="0 0 28 25"><path d="M0 0H28V17L14 25L0 17Z" fill="#f68d4d"/><text x="14" y="13" font-size="8" fill="#fff" text-anchor="middle" font-family="Open Sans, sans-serif">4</text></svg>
  <h2 class="abs pricing__title">Price title</h2>
  <table class="abs price-table">
    <thead><tr><th>NAME</th><th>PERCENTAGE</th><th>COUNTRY</th><th>INCOME</th><th>OUTCOME</th></tr></thead>
    <tbody>
      <tr><td>Lorem</td><td>38%</td><td>Etiam</td><td>2.000,30$</td><td>400,20$</td></tr>
      <tr><td>Sed</td><td>38%</td><td>Pellentesque</td><td>1.330,00$</td><td>900,40$</td></tr>
      <tr><td>Donec</td><td>38%</td><td>Vivamus</td><td>3.500,90$</td><td>100,50$</td></tr>
      <tr><td>Nullam</td><td>38%</td><td>Mauris</td><td>2.260,20$</td><td>1.020,30$</td></tr>
      <tr><td>Suspendisse</td><td>38%</td><td>Nullam</td><td>3.100,60$</td><td>1.120,00$</td></tr>
      <tr class="is-highlight"><td>Aenean</td><td>38%</td><td>Phasellus</td><td>4.230,10$</td><td>2.230,30$</td></tr>
      <tr class="is-total"><td>Mauris</td><td>38%</td><td>Aliquam</td><td>3.300,30$</td><td>579,30$</td></tr>
    </tbody>
  </table>
  <svg class="abs pricing__chart pricing__chart--a" viewBox="0 0 62 78">
    <rect x="0" y="38" width="9" height="40" fill="#d8392c"/>
    <rect x="13" y="0" width="9" height="78" fill="#f0a030"/>
    <rect x="26" y="20" width="9" height="58" fill="#4a8a3c"/>
    <rect x="39" y="36" width="9" height="42" fill="#7bb8b6"/>
    <rect x="52" y="49" width="9" height="29" fill="#2a6aa0"/>
  </svg>
  <svg class="abs pricing__chart pricing__chart--b" viewBox="0 0 62 78">
    <rect x="0" y="2" width="9" height="76" fill="#d8392c"/>
    <rect x="13" y="16" width="9" height="62" fill="#f0a030"/>
    <rect x="26" y="36" width="9" height="42" fill="#4a8a3c"/>
    <rect x="39" y="14" width="9" height="64" fill="#7bb8b6"/>
    <rect x="52" y="24" width="9" height="54" fill="#2a6aa0"/>
  </svg>
  <p class="abs pricing__note pricing__note--a">Nullam non elit vel est aliquet mollis non a mauris. Maecenas euismod aliquet risus ac posuere. Duis mollis metus quis enim viverra.</p>
  <p class="abs pricing__note pricing__note--b">Duis mollis metus quis enim viverra, ut cursus odio dictum. Proin condimentum fringilla dolor a ultricies.</p>
  <div class="abs page__footer"></div>
  <div class="abs page__tab"><span></span></div>
  <div class="abs page__url">www.brightharbor.com</div>
</section>

<section class="slide slide--thanks">
  <h2 class="abs thanks__title">Thank You</h2>
  <p class="abs thanks__sub">for your contribution at<br>the meetings</p>
  <svg class="abs thanks__divider" viewBox="0 0 262 10"><line x1="0" y1="5" x2="118" y2="5" stroke="#fff" stroke-width="0.8"/><circle cx="131" cy="5" r="3" fill="none" stroke="#fff" stroke-width="0.8"/><line x1="144" y1="5" x2="262" y2="5" stroke="#fff" stroke-width="0.8"/></svg>
  <p class="abs thanks__text">Lorem ipsum dolor sit amet, consectetur adipiscing<br>elit. Curabitur ultricies sagittis lorem, accumsan<br>dignissim mauris condimentum ut.</p>
  <div class="abs thanks__mark"></div>
</section>

<div class="abs brand-display">BRIGHTHARBOR</div>

</body>
</html>
```